Cloud Hosting Startup, and Panthers!

Hi!

We are quillbarrow.com

A new hosting service that aims to provide awesome hosting and a bit of development work for free to get people set up.

We have decided on a logo and a theme. Awesome Panthers.

So, we are all about Panthers =)

-

We greatly desire a super super cool vector scene for the homepage. We love mountains, blue mountains, and green grass. Panthers hiding in long grass or leaping through the air to accentuate the coolness of our service would also be most appreciated.

Panthers hiding amongst crisp blue mountains, or hanging out on snowy mountain peaks thinking Panther things.

Or in green grassy jungles, hiding next to rocks and scaring zebras.

Or something =)

-

For the sub pages we would just like a style guide, showing the standard h1,h2's and some other items for layout.

As you can see at quillbarrow.com we are almost ready for launch, we are web developers ourselves, and so we got the site design as far as we could.

We have our software written and ready for customers, however the site just doesn't tell you what its about from a glance! That's why we need you. So, Panthers, Cool cool, sweet Panthers to accentuate our cool new launch and hosting service.

We have included the vectors used and the site design as it stands. We would like to remain with the three items 'mini-panther', 'Standard Quill', and 'Epic Quill' from this page: quillbarrow.com/signup

Apart from the epic panthers, and some variation of the panthers used for the logo, we are not fully attached other elements. We have gone with a strong red white and black, but we are just wacky developers, we need your help!

Looking forward to some great designs! If you are inspired by Panthers and super cool web hosting, this project is for you.

Thanks!!

The Quillbarrow.com Team
Updates

Project payment has been guaranteed, we are committed to a result

Just a quick update based on a designer question:

We have spent many weeks of drinking coffee and coding, we have finished all the coding, all done!

If you take a look at Quillbarrow.com you can see the result.

Basically we are looking for someone to take what we have already done (files attached of all our work) and make it less like a developer designed it, which is what happened along the way =)

Help us obi wan kenobi ..
 

Basically, we are looking for increased awesome.

We have a really cool, cheap hosting and template product offering, we would love it if someone could breathe the life of Panther into it =)

Ok,

Thanks =)

Sorry, one more update =)

Basically we are not looking for an entire site re-design, the major thing is a cool scene for the homepage with panthers and mountains =)

We are just looking for a touch up, a polish, someone to give it the design magic that communicates the message in the copy we have written. We have worked out our product and completed it, we just need someone to help us bring it to the market.

Ok, thanks!

One final update then we will return to coding our Panther and leave you all alone =)

Our internet heroes are: http://www.vantorix.com/

We love them, their purple colour scheme makes us unhappy, but we so love their signup and plan selection process.

Ok!

Thanks so much, from Quillbarrow Team

Reason: Deadline has been extended one day to allow new designers time to prepare some panther concepts. We will also use the extra day to await funds transfer to increase the budget of the project and hopefully add a 2nd place prize (pixelguild fees permitting) Thanks everyone! Marcus Quillbarrow.com

Project budget has been upgraded, and a second place payment has been added

Thanks all!

Reason: Deadline extended a further one day, 1st prize and 2nd prize payments have been updated today, looking forward to submissions! Thanks everyone

Just an update, really great designs coming in, loving all the panther concepts =)

We will award the competition on the 21st, and we have two prizes now, we will award one based on visual design and appeal (the most stunning panther), and one based on use of copy and user interface (the easiest panther)

Ok!

Thanks, hope you have enjoyed designing, we have definitely enjoyed receiving designs to bring our idea to life

Thanks!!

Marcus

Quillbarrow

Sorry!

One more update, we have added a third prize now of $100 

We love the designs too much not to make use of them =)

Ok!

Last update =)

Thanks all

Hi All,

Wonderful work, thanks everyone for feedback and revisions

We have only one day of the competition left, we are asking now for final submissions, we have provided a style guide template here:

http://quillbarrow.com/web_final_template.psd

The team will judge the competition tomorrow, we have now 3 prizes and we will add 2 participation payments as a fourth prize as we have asked some designers for some strange requests =)

Ok!

Looking forward to final submissions with the home page and style guide, thanks again!

Marcus

Quillbarrow

Target Market(s)

Tech savvy people, but not tech geniuses, young fun people who at least know what web-hosting is

Industry/Entity Type

Software

Requirements
Must have
• - super super cool vector landscape for the homepage
- some number of sub pages, in accordance with the site structure as it stands

```html
<!DOCTYPE html>
<html lang="en">
<head>
<meta charset="utf-8">
<title>Quillbarrow – Plans</title>
<link rel="stylesheet" href="https://fonts.googleapis.com/css2?family=Noticia+Text:ital,wght@0,700;1,400;1,700&family=PT+Sans:wght@400;700&display=swap">
<style>
  :root {
    --red: #e85a4f;
    --ink: #333333;
    --footer: #2e2e2e;
    --sky: #72d4fb;
    --page: #f8f8f8;
    --feature-bg: #eeeeee;
    --white: #ffffff;
    --muted: #777777;
    --serif: "Noticia Text", Georgia, serif;
    --sans: "PT Sans", Arial, sans-serif;
  }
  * { box-sizing: border-box; margin: 0; padding: 0; }
  html, body { width: 977px; height: 1200px; overflow: hidden; }
  body { position: relative; background: var(--page); font-family: var(--sans); color: var(--ink); }

  .top-bar { position: absolute; left: 0; top: 0; width: 977px; height: 21px; background: var(--red); }
  .top-nav { position: absolute; right: 22px; top: 4px; font-size: 11px; line-height: 13px; color: var(--white); letter-spacing: .2px; }
  .top-nav a { color: var(--white); text-decoration: none; }
  .top-nav .active { color: var(--ink); }

  .hero { position: absolute; left: 0; top: 21px; width: 977px; height: 227px; overflow: hidden; }
  .hero-scene { position: absolute; inset: 0; background: linear-gradient(180deg, #343434 0%, #343434 22%, #4f8aa3 45%, var(--sky) 62%, var(--sky) 100%); }
  .brand { position: absolute; left: 66px; top: 50px; display: flex; align-items: center; gap: 7px; }
  .brand-dot { width: 14px; height: 14px; border-radius: 50%; background: var(--red); }
  .brand-name { font-family: var(--sans); font-weight: 700; font-size: 13px; color: var(--white); letter-spacing: .3px; }
  .promo-tag { position: absolute; left: 512px; top: 82px; width: 166px; height: 28px; background: var(--red); transform: rotate(-9deg); color: var(--white); font-family: var(--serif); font-style: italic; font-weight: 700; font-size: 6.5px; line-height: 9px; text-align: center; padding: 5px 10px; }
  .hero-title { position: absolute; left: 0; width: 910px; top: 121px; text-align: center; font-family: var(--serif); font-style: italic; font-weight: 700; font-size: 41px; line-height: 50px; color: var(--ink); }
  .hero-sub { position: absolute; left: 0; width: 910px; top: 170px; text-align: center; font-family: var(--serif); font-style: italic; font-size: 12.5px; line-height: 16px; color: var(--ink); letter-spacing: .3px; }

  .plan-art { position: absolute; background: linear-gradient(135deg, #e6e6e6, #d4d4d4); border-radius: 40% 50% 40% 50%; }
  .plan-art.mini { left: 251px; top: 452px; width: 82px; height: 44px; background: linear-gradient(135deg, #f08a80, var(--red)); }
  .plan-art.standard { left: 438px; top: 424px; width: 146px; height: 77px; }
  .plan-art.epic { left: 629px; top: 323px; width: 192px; height: 181px; }

  .plan-card { position: absolute; top: 517px; width: 209px; }
  .plan-card.mini { left: 166px; }
  .plan-card.standard { left: 387px; }
  .plan-card.epic { left: 608px; }
  .plan-name { height: 36px; background: var(--ink); color: var(--white); font-weight: 700; font-size: 14px; text-align: center; line-height: 36px; letter-spacing: .2px; }
  .plan-price { height: 70px; background: var(--white); text-align: center; line-height: 70px; color: var(--ink); }
  .plan-price .currency { font-size: 21px; }
  .plan-price .amount { font-size: 33px; font-weight: 700; }
  .plan-price .cents { font-size: 17px; font-weight: 700; vertical-align: 13px; }
  .plan-price .period { font-size: 21px; }
  .plan-features { height: 173px; background: var(--feature-bg); list-style: none; padding-top: 18px; text-align: center; font-family: var(--serif); font-style: italic; font-size: 12.5px; line-height: 24px; color: #555; }

  .footer { position: absolute; left: 0; top: 880px; width: 977px; height: 320px; background: var(--footer); }
  .footer-nav { position: absolute; left: 123px; top: 68px; list-style: none; font-size: 8.5px; font-weight: 700; line-height: 15.3px; }
  .footer-nav a { color: var(--white); text-decoration: none; }
  .footer-nav .active a { color: var(--red); }
  .social { position: absolute; left: 384px; top: 89px; display: flex; gap: 12px; }
  .social span { width: 27px; height: 27px; border-radius: 50%; background: #8a8a8a; border: 2px solid #5a5a5a; }
  .contact { position: absolute; left: 493px; top: 70px; width: 240px; }
  .contact h2 { text-align: center; font-size: 8px; line-height: 10px; font-weight: 700; color: var(--white); }
  .contact .field { position: absolute; background: var(--white); font-size: 6.5px; color: #999; padding: 5px; }
  .field.name { left: 0; top: 15px; width: 98px; height: 23px; }
  .field.email { left: 0; top: 40px; width: 98px; height: 22px; }
  .field.message { left: 102px; top: 15px; width: 138px; height: 47px; }
  .send { position: absolute; left: 202px; top: 73px; width: 38px; height: 14px; background: var(--red); color: var(--white); font-size: 7px; text-align: center; line-height: 14px; }
  .footer-brand { position: absolute; left: 0; width: 977px; top: 224px; display: flex; justify-content: center; align-items: center; gap: 8px; }
  .footer-brand .brand-dot { width: 16px; height: 16px; }
  .footer-brand .brand-name { font-size: 15px; }
  .copyright { position: absolute; left: 0; width: 977px; top: 254px; text-align: center; font-size: 8.5px; color: var(--muted); }
</style>
</head>
<body>
  <div class="top-bar">
    <nav class="top-nav"><a class="active" href="#">HOME</a> | <a href="#">PLANS&amp;PRINCING</a> | <a href="#">SIGN UP</a> | <a href="#">CONTACT</a></nav>
  </div>

  <header class="hero">
    <div class="hero-scene" role="img" aria-label="Dark sky over a light blue mountain ridge"></div>
    <div class="brand"><span class="brand-dot"></span><span class="brand-name">QUILLBARROW</span></div>
    <div class="promo-tag">Template, Domain, Hosting and Email package for under $5</div>
    <h1 class="hero-title">Quill Plans</h1>
    <p class="hero-sub">Quill plans include hosting, email, and template configuration.</p>
  </header>

  <main>
    <div class="plan-art mini" role="img" aria-label="Small red leaping big cat"></div>
    <div class="plan-art standard" role="img" aria-label="Outlined leaping big cat"></div>
    <div class="plan-art epic" role="img" aria-label="Winged leaping big cat line drawing"></div>

    <section class="plan-card mini">
      <h2 class="plan-name">MINI QUILL</h2>
      <div class="plan-price"><span class="currency">$</span><span class="amount">3</span><span class="cents">.99</span><span class="period">/mo.</span></div>
      <ul class="plan-features"><li>1GB Storage Space</li><li>2 E-mail Accounts</li><li>4 Content Management Software</li><li>4 Free Template Integration</li></ul>
    </section>
    <section class="plan-card standard">
      <h2 class="plan-name">STANDARD QUILL</h2>
      <div class="plan-price"><span class="currency">$</span><span class="amount">8</span><span class="cents">.99</span><span class="period">/mo.</span></div>
      <ul class="plan-features"><li>5GB Storage Space</li><li>5 E-mail Accounts</li><li>4 Content Management Software</li><li>4 Free Template Integration</li></ul>
    </section>
    <section class="plan-card epic">
      <h2 class="plan-name">EPIC QUILL</h2>
      <div class="plan-price"><span class="currency">$</span><span class="amount">24</span><span class="cents">.99</span><span class="period">/mo.</span></div>
      <ul class="plan-features"><li>15GB Storage Space</li><li>15 E-mail Accounts</li><li>Free Domain</li><li>4 Content Management Software</li><li>4 Free Template Integration</li></ul>
    </section>
  </main>

  <footer class="footer">
    <ul class="footer-nav">
      <li class="active"><a href="#">HOME</a></li>
      <li><a href="#">PLANS&amp;PRINCING</a></li>
      <li><a href="#">SIGN UP</a></li>
      <li><a href="#">CONTACT</a></li>
    </ul>
    <div class="social"><span></span><span></span></div>
    <form class="contact">
      <h2>CONTACT QUILL</h2>
      <div class="field name">Contact Name</div>
      <div class="field email">Contact Email</div>
      <div class="field message">Message</div>
      <div class="send">Send</div>
    </form>
    <div class="footer-brand"><span class="brand-dot"></span><span class="brand-name">QUILLBARROW</span></div>
    <p class="copyright">2013 | Quillbarrow.com</p>
  </footer>
</body>
</html>
```